Tamarack Hearth Partners Business Card

Looking for a new business card layout. We are a real estate firm w/ a logo, old design attached. Must keep the same elements on there, just need a fresh look and possible some foil accents. Looking for a simpler design w/ more modern style.

Target Market(s)

Real Estate clients

Industry/Entity Type

Real Estate Agent

Contact Information for Business Card

see attached

Font styles to use
Sans Serif

Requirements
Must have
• all elements on current biz card
Nice to have
• modern look, simpler than we have!
Should not have
• no serif fonts

```html
<!DOCTYPE html>
<html lang="en">
<head>
<meta charset="utf-8">
<title>Tamarack Hearth Partners – Business Card</title>
<link href="https://fonts.googleapis.com/css2?family=Lato:wght@400;700&display=swap" rel="stylesheet">
<style>
  :root {
    --backdrop: #e6e7ea;
    --card: #2a2a2c;
    --accent: #22b3bf;
    --ink: #f4f4f4;
    --photo-light: #e9d6b4;
    --photo-dark: #a88d68;
  }
  * { margin: 0; padding: 0; box-sizing: border-box; }
  html, body {
    width: 1058px; height: 1200px; overflow: hidden;
    background: var(--backdrop);
    font-family: "Lato", sans-serif;
  }
  .canvas { position: relative; width: 1058px; height: 1200px; }

  .card { position: absolute; background: var(--card); border-radius: 40px; }

  .card-front { left: 328px; top: 33px; width: 399px; height: 701px; color: var(--ink); text-align: center; }
  .portrait { position: absolute; left: 115px; top: 62px; width: 192px; height: 192px; }
  .agent-name {
    position: absolute; top: 326px; left: 0; width: 100%;
    font-size: 27px; font-weight: 700; letter-spacing: 2.5px; color: var(--accent);
  }
  .agent-title { position: absolute; top: 357px; left: 0; width: 100%; font-size: 15px; }
  .address { position: absolute; top: 446px; left: 0; width: 100%; font-size: 18.5px; line-height: 24px; }
  .divider { position: absolute; top: 515px; left: 143px; width: 112px; height: 1.5px; background: var(--accent); }
  .contact-list { position: absolute; top: 538px; left: 0; width: 100%; list-style: none; font-size: 18.5px; line-height: 25.5px; }
  .contact-list .label { color: var(--accent); }
  .contact-list .web { margin-top: 3px; }

  .card-back { left: 177px; top: 760px; width: 701px; height: 400px; }
  .brand-name {
    position: absolute; top: 168px; left: 0; width: 100%; text-align: center;
    font-size: 40px; font-weight: 700; letter-spacing: 3px; text-transform: uppercase;
    color: var(--accent);
  }
</style>
</head>
<body>
<main class="canvas">
  <section class="card card-front">
    <svg class="portrait" viewBox="0 0 192 192" role="img" aria-label="Portrait photo of the agent">
      <defs>
        <radialGradient id="portrait-tone" cx="50%" cy="40%" r="65%">
          <stop offset="0%" stop-color="var(--photo-light)"/>
          <stop offset="100%" stop-color="var(--photo-dark)"/>
        </radialGradient>
      </defs>
      <circle cx="96" cy="96" r="96" fill="url(#portrait-tone)"/>
    </svg>
    <h1 class="agent-name">Dana Whitlock</h1>
    <p class="agent-title">Principal Broker</p>
    <p class="address">210 NE 4th<br>st Sisters, OR 97759</p>
    <div class="divider"></div>
    <ul class="contact-list">
      <li><span class="label">Cell:</span> 555 310 4827</li>
      <li><span class="label">Office:</span> 555 310 7390</li>
      <li><span class="label">Email:</span> dana@tamarackhp.com</li>
      <li class="web">TamarackHearth-Homes.com</li>
    </ul>
  </section>

  <section class="card card-back">
    <p class="brand-name">Tamarack Hearth Partners</p>
  </section>
</main>
</body>
</html>
```